MORLIVEX Hemp based Pet Brand that growns it's own premium hemp and creates amazing pet products.

We need packaging designed for a new company based in South West Florida. We grow our own hemp with our other company Crest 4 Vale and use the harvest to make our hemp based pet products. Our initial products are pet treats that include Soft Chews and Calming Chews. The bags come in two different sizes. Regular bag being 7x10.25 inches and Small bag 4.25X6.25 inches. We also need a tincture box and label created. We want packaging that will catch the eye of the consumer and colors that compliment our logo. Dropper label size is 4x1.75 inches and the milligram of CBD is 1500. We have attached our manufacturers packaging and would like you to coppy everything other than their overall design and logo. Use default UPC and QR code, which we can replace later in the Ai file. Please see all the attached documents and please ask me if you have any questions. The final design should communicate a premium product that stand our from the rest. Something that catches the eye of the consumer by its premium appearance. Packaging is everything so I hope you can use your creative skills to create something special!

Target Market(s)

Pet owners

Font styles to use
Serif
Sans Serif

Colors
0054AA
0677BA
7BADD7
CADEEF
E8F1F8
0094D4
00A9DD
6FCCEA
C7EBF8
E9F6FB
EE7325
F08F49
F5BC92
FAE3D3
FDF4ED

Requirements
Must have
• Stand out design. Premium feel. Imagine shopping for something for your pet and seeing a brand that POPS and just looks like a good product because the packaging is so good.
Nice to have
• Modern mature feel
Should not have
• Cartoony feeling. Do not use baby blue everywhere. Do not include pictures of people in the packaging

```html
<!DOCTYPE html>
<html lang="en">
<head>
<meta charset="utf-8">
<title>MORLIVEX Soft Chews – Pouch Front</title>
<link rel="stylesheet" href="https://fonts.googleapis.com/css2?family=Teko:wght@400;500;600&display=swap">
<style>
  :root {
    --bg: #ffffff;
    --pouch: #161616;
    --pouch-edge: #262626;
    --orange: #EE7325;
    --orange-mid: #F08F49;
    --orange-light: #F5BC92;
    --badge-blue: #6FCCEA;
    --badge-ring: #ffffff;
    --ink-dark: #1a1a1a;
  }
  * { margin: 0; padding: 0; box-sizing: border-box; }
  html, body { width: 1200px; height: 1200px; overflow: hidden; background: var(--bg); }
  .canvas { position: relative; width: 1200px; height: 1200px; background: var(--bg); }
  .pouch {
    position: absolute; left: 328px; top: 100px; width: 534px; height: 928px;
    background: linear-gradient(90deg, var(--pouch-edge) 0%, var(--pouch) 12%, var(--pouch) 88%, var(--pouch-edge) 100%);
    border-radius: 10px 10px 6px 6px;
    font-family: "Teko", "Oswald", sans-serif;
    color: var(--orange);
  }
  .zip-seal { position: absolute; left: 0; right: 0; top: 70px; height: 2px; background: #2e2e2e; }
  .zip-seal.lower { top: 84px; }
  .side-band { position: absolute; top: 160px; height: 40px; width: 72px; background: linear-gradient(90deg, var(--orange), var(--orange-mid)); }
  .side-band.left { left: 0; }
  .side-band.right { right: 0; }
  .title {
    position: absolute; left: 0; right: 0; top: 150px; text-align: center;
    font-weight: 500; text-transform: uppercase; line-height: 0.92;
    background: linear-gradient(180deg, var(--orange-mid), var(--orange));
    -webkit-background-clip: text; background-clip: text; color: transparent;
  }
  .title .brand { display: block; font-size: 98px; letter-spacing: 3px; }
  .title .product { display: block; font-size: 108px; letter-spacing: 3px; }
  .badge {
    position: absolute; left: 107px; top: 347px; width: 320px; height: 320px;
    border-radius: 50%; background: var(--badge-blue); border: 6px solid var(--badge-ring);
    display: flex; align-items: center; justify-content: center;
  }
  .badge-name { font-family: "Teko", sans-serif; font-weight: 600; font-size: 64px; letter-spacing: 4px; color: var(--ink-dark); }
  .contact { position: absolute; left: 0; right: 0; top: 716px; text-align: center; font-weight: 400; font-size: 30px; line-height: 1.1; letter-spacing: 1px; }
  .count { position: absolute; left: 0; right: 0; top: 802px; text-align: center; font-size: 18px; letter-spacing: 1px; }
  .rule { position: absolute; left: 0; right: 0; top: 832px; height: 5px; background: var(--orange); }
  .web-band {
    position: absolute; left: 0; right: 0; top: 842px; height: 26px;
    background: linear-gradient(90deg, var(--orange) 0%, var(--orange-light) 50%, var(--orange) 100%);
    text-align: center; font-size: 18px; line-height: 30px; color: var(--ink-dark); letter-spacing: 1px;
  }
</style>
</head>
<body>
<div class="canvas">
  <section class="pouch" aria-label="MORLIVEX Soft Chews pouch front">
    <div class="zip-seal"></div>
    <div class="zip-seal lower"></div>
    <div class="side-band left"></div>
    <div class="side-band right"></div>
    <h1 class="title"><span class="brand">MORLIVEX</span><span class="product">Soft Chews</span></h1>
    <div class="badge"><span class="badge-name">MORLIVEX</span></div>
    <p class="contact">Tel: (555) 201-4836<br>218 Marsh Lane, Cypress Bay, FL 33990</p>
    <p class="count">Net CT. 60 | Net Wt. 10.6 oz</p>
    <div class="rule"></div>
    <div class="web-band">www.morlivex.com</div>
  </section>
</div>
</body>
</html>
```